TIDAL VERGE needs bisness cards pronto

Bisness name is "TIDAL VERGE" new bisness the bisness includes lawn mowing, garden matanace, and any jobs around the house.
I need a card that is colorful and vibrant and the bisness of lawn mowing maybe with some nature with it. It also needs my contact details"Darren Quellby mobile 0413562049 call for free quote and email norma.vance@fernmail.com.au and a catchy tag line

Industry/Entity Type

House

Requirements
Must have
• Bisness name "TIDAL VERGE"
Contact details "0413562049"
Email norma.vance@fernmail.com.au
Call for free quote

```html
<!DOCTYPE html>
<html lang="en">
<head>
<meta charset="utf-8">
<title>TIDAL VERGE – Business Card</title>
<link rel="stylesheet" href="https://fonts.googleapis.com/css2?family=Roboto+Condensed:wght@400;700&display=swap">
<style>
  :root {
    --page-bg: #ffffff;
    --card-bg: #ffffff;
    --card-border: #5a5a5a;
    --lawn-light: #a2d13f;
    --lawn-mid: #94ca38;
    --lawn-dark: #86c133;
    --lawn-edge: #6fa72a;
    --ink: #333333;
    --ink-strong: #111111;
    --title-ink: #ffffff;
  }
  * { box-sizing: border-box; margin: 0; padding: 0; }
  html, body {
    width: 1200px;
    height: 657px;
    overflow: hidden;
    background: var(--page-bg);
  }
  .canvas {
    position: relative;
    width: 1200px;
    height: 657px;
  }
  .business-card {
    position: absolute;
    left: 353px;
    top: 160px;
    width: 473px;
    height: 308px;
    background: var(--card-bg);
    border: 1px solid var(--card-border);
    overflow: hidden;
    font-family: "Roboto Condensed", "Arial Narrow", sans-serif;
  }
  .lawn-panel {
    position: absolute;
    left: 0;
    top: 0;
    width: 237px;
    height: 100%;
    background: linear-gradient(135deg, var(--lawn-light), var(--lawn-mid) 55%, var(--lawn-dark));
  }
  .brand-block {
    position: absolute;
    left: 0;
    top: 0;
    width: 237px;
    height: 100%;
    display: flex;
    flex-direction: column;
    align-items: center;
    justify-content: center;
    padding-top: 10px;
    color: var(--title-ink);
    text-align: center;
  }
  .brand-name {
    font-weight: 700;
    font-size: 30px;
    line-height: 1;
    letter-spacing: 1px;
    white-space: nowrap;
  }
  .brand-tagline {
    margin-top: 8px;
    font-weight: 400;
    font-size: 14px;
    line-height: 1;
    white-space: nowrap;
  }
  .contact-block {
    position: absolute;
    right: 13px;
    top: 25px;
    text-align: right;
    font-size: 16px;
    line-height: 20px;
    color: var(--ink);
    list-style: none;
  }
  .quote-badge {
    position: absolute;
    left: 250px;
    top: 102px;
    width: 198px;
    height: 198px;
  }
  .quote-badge svg { display: block; }
  .quote-text {
    position: absolute;
    inset: 0;
    display: flex;
    align-items: center;
    justify-content: center;
    font-weight: 700;
    font-size: 19px;
    color: var(--ink-strong);
    white-space: nowrap;
    padding-bottom: 14px;
  }
</style>
</head>
<body>
  <main class="canvas">
    <article class="business-card">
      <div class="lawn-panel" role="img" aria-label="Mown lawn stripes in fresh greens"></div>
      <header class="brand-block">
        <h1 class="brand-name">TIDAL VERGE</h1>
        <p class="brand-tagline">Neat edges, happy yards</p>
      </header>

      <ul class="contact-block">
        <li class="contact-name">Darren Quellby</li>
        <li class="contact-phone">0413562049</li>
        <li class="contact-email">norma.vance@fernmail.com.au</li>
      </ul>

      <div class="quote-badge">
        <svg width="198" height="198" viewBox="0 0 198 198" role="img" aria-label="Round badge of mown lawn stripes in fresh greens">
          <defs>
            <linearGradient id="badge-lawn" x1="0" y1="0" x2="1" y2="1">
              <stop offset="0" stop-color="var(--lawn-light)"/>
              <stop offset="0.55" stop-color="var(--lawn-mid)"/>
              <stop offset="1" stop-color="var(--lawn-dark)"/>
            </linearGradient>
          </defs>
          <circle cx="99" cy="99" r="98" fill="url(#badge-lawn)" stroke="var(--lawn-edge)" stroke-width="1"/>
        </svg>
        <p class="quote-text">Call for free quote!</p>
      </div>
    </article>
  </main>
</body>
</html>
```